Business card design and logo for hot water plumbing business

I need a logo and business card for my business which installs hot water heaters
Must have on front:
Paramount Hot Water Services
Gareth Pellow
0498163204

Either front or back:
gareth@paramounthotwaterservices-example.com.au
ABN 48207153690
Licence No 538412K

On the back in point form:
Supply and installation of
• electric storage
• gas storage/instantaneous
• heat pumps
• solar heaters

Iv provided 3 examples of cards I like but open to different ideas.

```html
<!DOCTYPE html>
<html lang="en">
<head>
<meta charset="utf-8">
<title>Paramount Hot Water Services – Business Card</title>
<link rel="stylesheet" href="https://fonts.googleapis.com/css2?family=Jost:wght@400;500;600&display=swap">
<style>
  :root {
    --brand-blue: #1f5fd6;
    --brand-blue-light: #3d7ff0;
    --brand-red: #ea1c24;
    --card-white: #ffffff;
    --card-tint: #eef1f7;
    --page-bg: #e4e6ea;
    --band-text: #ffffff;
  }
  * { box-sizing: border-box; margin: 0; padding: 0; }
  html, body {
    width: 1200px; height: 674px; overflow: hidden;
    background: var(--page-bg);
    font-family: "Jost", "Futura", sans-serif;
  }
  .sheet {
    width: 1200px; height: 674px;
    display: flex; align-items: center; justify-content: center; gap: 60px;
  }
  .card {
    position: relative;
    width: 520px; height: 297px;
    background: linear-gradient(180deg, var(--card-tint) 0%, var(--card-white) 45%);
    box-shadow: 0 6px 18px rgba(0,0,0,0.18);
    overflow: hidden;
  }
  .card-band {
    position: absolute; inset: 0;
    width: 100%; height: 100%;
  }
  /* Front */
  .brand {
    position: absolute; top: 30px; left: 26px;
    display: flex; align-items: center; gap: 10px;
    font-weight: 500; font-size: 23px; letter-spacing: 0.3px;
    text-transform: uppercase; color: var(--brand-blue);
    white-space: nowrap;
  }
  .brand-dot {
    width: 22px; height: 22px; border-radius: 50%;
    background: var(--brand-blue); flex: none;
  }
  .contact-name {
    position: absolute; top: 96px; left: 0; right: 0;
    text-align: center;
    font-variant: small-caps; font-weight: 500;
    font-size: 34px; color: var(--brand-blue); letter-spacing: 0.5px;
  }
  .contact-phone {
    position: absolute; top: 140px; left: 0; right: 0;
    text-align: center;
    font-weight: 600; font-size: 20px; color: var(--brand-red);
  }
  .contact-details {
    position: absolute; top: 212px; left: 30px;
    color: var(--band-text); font-size: 15px; line-height: 22px;
    text-align: center;
  }
  /* Back */
  .services {
    position: absolute; top: 30px; left: 0; right: 0;
    text-align: center; text-transform: uppercase;
  }
  .services-title {
    font-weight: 600; font-size: 22px; color: var(--brand-red);
    letter-spacing: 0.6px; margin-bottom: 10px;
  }
  .services-list {
    list-style: none;
    font-weight: 500; font-size: 16px; line-height: 26px;
    color: var(--brand-blue); letter-spacing: 0.4px;
  }
  .services-list li::before { content: "• "; }
</style>
</head>
<body>
<main class="sheet">

  <section class="card card-front" aria-label="Business card front">
    <svg class="card-band" viewBox="0 0 520 297" preserveAspectRatio="none" aria-hidden="true">
      <path d="M0,168 Q300,188 520,240 L520,297 L0,297 Z" fill="var(--brand-blue)"/>
      <path d="M0,160 Q300,180 520,232" fill="none" stroke="var(--brand-red)" stroke-width="4"/>
    </svg>
    <div class="brand"><span class="brand-dot"></span><span class="brand-name">Paramount Hot Water Services</span></div>
    <div class="contact-name">Gareth Pellow</div>
    <div class="contact-phone">0498163204</div>
    <div class="contact-details">
      <div>gareth@paramounthotwaterservices-example.com.au</div>
      <div>ABN 48207153690</div>
      <div>Licence No 538412K</div>
    </div>
  </section>

  <section class="card card-back" aria-label="Business card back">
    <svg class="card-band" viewBox="0 0 520 297" preserveAspectRatio="none" aria-hidden="true">
      <path d="M0,232 Q260,250 520,262 L520,297 L0,297 Z" fill="var(--brand-blue)"/>
      <path d="M0,224 Q260,242 520,254" fill="none" stroke="var(--brand-red)" stroke-width="4"/>
    </svg>
    <div class="services">
      <h2 class="services-title">Supply and installation of</h2>
      <ul class="services-list">
        <li>Electric storage</li>
        <li>Gas storage/instantaneous</li>
        <li>Heat pumps</li>
        <li>Solar heaters</li>
      </ul>
    </div>
  </section>

</main>
</body>
</html>
```